colour pencil case design

I am looking for a design for the front of a pencil case. The pencil case has 2 versions, 1 white fabric and 1 black fabric. The design should have 2 versions, eg. white word on black fabric and black words on white fabric. Its for children and teenagers’ aged 7 to 18. I can have 2 separate designs.
The pencil case is 22cm by 14cm. So the size of the image should be 18cm by 11cm. Files should be in png format and already in the correct size.
It must have the word “Believe”in big size. The letter b can be in capps or small letter. Prefer the font used in
I am looking for a background or image that can represent the phrase. If the design is good, I am open to also black and white theme.
Can also be black and white or colour... I have attached the font that I like for the main word "Believe". https://www.quorvanta.net/gallery/583017462/Free-Font-Abelisa-Modern-Script. Or you can use this font for the word Believe as well…. "Playlist script
Besides the word Believe, you should have the sentence ‘you can and you will”. It can be all in capps or small letter. (smaller size and different font from your word.
Target Market(s)
children and teenagers
Industry/Entity Type
tuition
Requirements
Must have
- The word Believe and the phrase I can and I will
Nice to have
- Some colourful pictures that can represent the phrase

```html
<!DOCTYPE html>
<html lang="en">
<head>
<meta charset="utf-8">
<title>Believe – Pencil Case Prints</title>
<link rel="stylesheet" href="https://fonts.googleapis.com/css2?family=Kaushan+Script&family=Raleway:wght@400&display=swap">
<style>
  :root {
    --page: #ffffff;
    --fabric-light: #f4f4f4;
    --fabric-dark: #141414;
    --ink-dark: #0d0d0d;
    --ink-light: #ffffff;
    --crayon-pink: #ef7b86;
    --crayon-teal: #1aa3b2;
    --crayon-blue: #2f7fd0;
    --crayon-sea: #15b3a6;
    --crayon-lime: #7cc242;
    --crayon-green: #3cae48;
    --crayon-brown: #8a6a2c;
    --crayon-orange: #f06b22;
  }
  * { margin: 0; padding: 0; box-sizing: border-box; }
  html, body {
    width: 997px;
    height: 1200px;
    overflow: hidden;
    background: var(--page);
  }
  .sheet {
    position: relative;
    width: 997px;
    height: 1200px;
  }
  .print {
    position: absolute;
    left: 62px;
    width: 877px;
    height: 535px;
    overflow: hidden;
    box-shadow: 0 5px 7px rgba(0, 0, 0, 0.35);
  }
  .print--white { top: 42px; background: var(--fabric-light); color: var(--ink-dark); }
  .print--black { top: 607px; background: var(--fabric-dark); color: var(--ink-light); }
  .crayon-strokes {
    position: absolute;
    inset: 0;
    width: 100%;
    height: 100%;
  }
  .headline {
    position: absolute;
    left: 0;
    right: 0;
    top: 48px;
    text-align: center;
    font-family: "Kaushan Script", cursive;
    font-size: 245px;
    line-height: 1;
    letter-spacing: -4px;
    padding-right: 40px;
  }
  .tagline {
    position: absolute;
    left: 0;
    right: 0;
    top: 366px;
    text-align: center;
    font-family: "Raleway", sans-serif;
    font-weight: 400;
    font-size: 28px;
    letter-spacing: 0.5px;
    padding-right: 40px;
  }
  .stroke-pink { fill: var(--crayon-pink); }
  .stroke-teal { fill: var(--crayon-teal); }
  .stroke-blue { fill: var(--crayon-blue); }
  .stroke-sea { fill: var(--crayon-sea); }
  .stroke-lime { fill: var(--crayon-lime); }
  .stroke-green { fill: var(--crayon-green); }
  .stroke-brown { fill: var(--crayon-brown); }
  .stroke-orange { fill: var(--crayon-orange); }
</style>
</head>
<body>
<main class="sheet">

  <section class="print print--white" aria-label="Believe print on white fabric">
    <svg class="crayon-strokes" viewBox="0 0 730 445" preserveAspectRatio="none" aria-hidden="false">
      <polygon class="stroke-pink" role="img" aria-label="Pink crayon scribble" points="0,0 240,0 230,30 120,75 0,125"/>
      <polygon class="stroke-teal" role="img" aria-label="Teal crayon scribble" points="0,300 230,290 235,330 200,370 230,395 150,445 0,445"/>
      <polygon class="stroke-blue" role="img" aria-label="Blue crayon scribble" points="520,8 730,2 730,32 530,40"/>
      <polygon class="stroke-blue" role="img" aria-label="Blue crayon scribble" points="540,88 730,80 730,108 550,112"/>
      <polygon class="stroke-sea" role="img" aria-label="Teal crayon scribble" points="640,135 730,128 730,162 650,168"/>
      <polygon class="stroke-sea" role="img" aria-label="Sea green crayon scribble" points="650,182 730,176 730,212 660,216"/>
      <polygon class="stroke-lime" role="img" aria-label="Lime crayon scribble" points="610,248 730,242 730,272 620,276"/>
      <polygon class="stroke-green" role="img" aria-label="Green crayon scribble" points="590,292 730,282 730,330 600,335"/>
      <polygon class="stroke-brown" role="img" aria-label="Brown crayon scribble" points="530,382 730,375 730,395 540,402"/>
      <polygon class="stroke-orange" role="img" aria-label="Orange crayon scribble" points="640,410 730,398 730,445 660,445"/>
    </svg>
    <h1 class="headline">Believe</h1>
    <p class="tagline">YOU CAN AND YOU WILL</p>
  </section>

  <section class="print print--black" aria-label="Believe print on black fabric">
    <svg class="crayon-strokes" viewBox="0 0 730 445" preserveAspectRatio="none" aria-hidden="false">
      <polygon class="stroke-pink" role="img" aria-label="Pink crayon scribble" points="0,0 240,0 230,30 120,75 0,125"/>
      <polygon class="stroke-teal" role="img" aria-label="Teal crayon scribble" points="0,300 230,290 235,330 200,370 230,395 150,445 0,445"/>
      <polygon class="stroke-blue" role="img" aria-label="Blue crayon scribble" points="520,8 730,2 730,32 530,40"/>
      <polygon class="stroke-blue" role="img" aria-label="Blue crayon scribble" points="540,88 730,80 730,108 550,112"/>
      <polygon class="stroke-sea" role="img" aria-label="Teal crayon scribble" points="640,135 730,128 730,162 650,168"/>
      <polygon class="stroke-sea" role="img" aria-label="Sea green crayon scribble" points="650,182 730,176 730,212 660,216"/>
      <polygon class="stroke-lime" role="img" aria-label="Lime crayon scribble" points="610,248 730,242 730,272 620,276"/>
      <polygon class="stroke-green" role="img" aria-label="Green crayon scribble" points="590,292 730,282 730,330 600,335"/>
      <polygon class="stroke-brown" role="img" aria-label="Brown crayon scribble" points="530,382 730,375 730,395 540,402"/>
      <polygon class="stroke-orange" role="img" aria-label="Orange crayon scribble" points="640,410 730,398 730,445 660,445"/>
    </svg>
    <h2 class="headline">Believe</h2>
    <p class="tagline">YOU CAN AND YOU WILL</p>
  </section>

</main>
</body>
</html>
```